Watch brand needs new business cards

Fernhollow Clock Company are looking for a new business card design incorporating our logo and brand colours as per our website.

Design should be 90x55mm with 3mm print margin from edges and 3mm external bleed.

Card should be double sided, e.g. logo one side, personal details on the other.

Logo will be provided as a vector.

The card must be able to show:
- Staff name
- Position
- Office Address
- Email
- Telephone number
- Website address

Final work must be provided in an editable format to allow us to add staff details (e.g. an AI or PSD file).

Industry/Entity Type

Business

```html
<!DOCTYPE html>
<html lang="en">
<head>
<meta charset="utf-8">
<title>Fernhollow Clock Company – Business Cards</title>
<link rel="stylesheet" href="https://fonts.googleapis.com/css2?family=Open+Sans:wght@400;600;700&display=swap">
<style>
  :root {
    --ink: #222222;
    --card-dark: #262626;
    --paper: #ffffff;
    --stage: #ecebe8;
    --muted: #3a3a3a;
  }
  * { box-sizing: border-box; margin: 0; padding: 0; }
  html, body {
    width: 1200px; height: 900px; overflow: hidden;
    background: var(--stage);
    font-family: "Open Sans", Arial, sans-serif;
    color: var(--ink);
  }
  .canvas {
    width: 1200px; height: 900px;
    display: flex; align-items: center; justify-content: center; gap: 44px;
  }
  .card {
    width: 540px; height: 330px;
    position: relative; overflow: hidden;
    box-shadow: 0 6px 18px rgba(0,0,0,.18);
  }

  /* Details side */
  .card--details { display: flex; background: var(--paper); }
  .details-panel {
    width: 58%; padding: 46px 30px 30px 36px;
    display: flex; flex-direction: column;
  }
  .staff-name {
    font-weight: 700; font-size: 27px; letter-spacing: .5px; line-height: 1;
  }
  .staff-role {
    font-size: 14px; letter-spacing: 2px; margin: 6px 0 0 64px; color: var(--muted);
  }
  .divider { height: 2px; background: var(--ink); margin: 22px 0 20px; }
  .contact-list { list-style: none; display: flex; flex-direction: column; gap: 14px; }
  .contact-item { display: flex; align-items: flex-start; gap: 14px; font-size: 13px; line-height: 1.35; }
  .contact-icon { width: 18px; height: 18px; flex: none; fill: var(--ink); margin-top: 1px; }
  .brand-panel {
    width: 42%; background: var(--card-dark); color: var(--paper);
    display: flex; flex-direction: column; align-items: center; justify-content: center; gap: 26px;
  }
  .brand-mark {
    width: 118px; height: 118px; border-radius: 50%;
    border: 5px solid var(--paper);
    display: flex; align-items: center; justify-content: center; text-align: center;
    font-weight: 600; font-size: 13px; letter-spacing: 1px; line-height: 1.3;
  }
  .website { font-size: 13px; letter-spacing: .3px; }

  /* Brand side */
  .card--brand {
    background: var(--card-dark); color: var(--paper);
    display: flex; flex-direction: column; align-items: center; justify-content: center; gap: 22px;
  }
  .brand-circle { width: 88px; height: 88px; border-radius: 50%; border: 5px solid var(--paper); }
  .brand-name {
    font-weight: 600; font-size: 38px; letter-spacing: 3px; line-height: 1; text-align: center;
  }
  .brand-sub { font-weight: 600; font-size: 15px; letter-spacing: 6px; }
</style>
</head>
<body>
<main class="canvas">
  <section class="card card--details" aria-label="Business card, staff details side">
    <div class="details-panel">
      <h1 class="staff-name">LIAM CARTER</h1>
      <p class="staff-role">Manager</p>
      <div class="divider"></div>
      <ul class="contact-list">
        <li class="contact-item">
          <svg class="contact-icon" viewBox="0 0 24 24" aria-hidden="true"><path d="M6.6 10.8a15.1 15.1 0 0 0 6.6 6.6l2.2-2.2c.3-.3.7-.4 1-.2 1.1.4 2.3.6 3.6.6.6 0 1 .4 1 1V20c0 .6-.4 1-1 1A17 17 0 0 1 3 4c0-.6.4-1 1-1h3.5c.6 0 1 .4 1 1 0 1.3.2 2.5.6 3.6.1.3 0 .7-.2 1z"/></svg>
          <span>(+61 3) 5550 1284</span>
        </li>
        <li class="contact-item">
          <svg class="contact-icon" viewBox="0 0 24 24" aria-hidden="true"><circle cx="12" cy="12" r="10"/><path d="M2 12h20M12 2c3 3 3 17 0 20M12 2c-3 3-3 17 0 20" stroke="#fff" stroke-width="1.4" fill="none"/></svg>
          <span>support@fernhollowclock.com</span>
        </li>
        <li class="contact-item">
          <svg class="contact-icon" viewBox="0 0 24 24" aria-hidden="true"><path d="M12 2a7 7 0 0 0-7 7c0 5.2 7 13 7 13s7-7.8 7-13a7 7 0 0 0-7-7zm0 9.5A2.5 2.5 0 1 1 12 6.5a2.5 2.5 0 0 1 0 5z"/></svg>
          <span>Fernhollow Clock Company Pty Ltd<br>Suite 4 &nbsp;Level 2 &nbsp;17 Alder Lane<br>Brookvale VIC 3099</span>
        </li>
      </ul>
    </div>
    <div class="brand-panel">
      <div class="brand-mark">FERNHOLLOW</div>
      <p class="website">fernhollowclock.com.au</p>
    </div>
  </section>

  <section class="card card--brand" aria-label="Business card, brand side">
    <div class="brand-circle"></div>
    <p class="brand-name">FERNHOLLOW</p>
    <p class="brand-sub">CLOCK COMPANY</p>
  </section>
</main>
</body>
</html>
```